Flyer for Choir Christmas Concert

Need colorful flyer for Christmas Choir Concert.

Requirements
Should not have
• I don't like musical symbols incorporated into the design.

```html
<!DOCTYPE html>
<html lang="en">
<head>
<meta charset="utf-8">
<title>Love and Joy – Christmas Choir Concert Flyer</title>
<link rel="stylesheet" href="https://fonts.googleapis.com/css2?family=Crimson+Text:wght@400;600;700&family=Yellowtail&family=Dancing+Script:wght@700&family=Oswald:wght@600&family=Montserrat:wght@400;500&family=Roboto:wght@400;500&display=swap">
<style>
  :root {
    --backdrop: #2e3033;
    --paper: #ffffff;
    --ice: #d9f2fb;
    --sky: #bfe8f7;
    --navy: #1d2a6b;
    --plum: #3b2266;
    --violet: #4b2a7e;
    --flame: #d9381e;
    --ink: #1c1c22;
    --leather: #4a2a17;
    --leather-light: #6a3e22;
    --stitch: #d9b28a;
  }
  * { box-sizing: border-box; margin: 0; padding: 0; }
  html, body { width: 1200px; height: 1200px; overflow: hidden; }
  body { background: var(--backdrop); position: relative; }

  .flyer {
    position: absolute; left: 150px; top: 17px;
    width: 900px; height: 1166px;
    background:
      radial-gradient(ellipse at 85% 5%, #ffffff 0%, rgba(255,255,255,0) 45%),
      linear-gradient(180deg, #ffffff 0%, var(--ice) 40%, var(--sky) 70%, #eaf7fc 84%, #ffffff 84%);
    overflow: hidden;
    color: var(--ink);
  }

  .ornament-art {
    position: absolute; left: 0; top: 0; width: 420px; height: 800px;
    background:
      radial-gradient(circle at 210px 420px, rgba(122,88,200,0.55) 0 60px, rgba(122,88,200,0) 110px),
      radial-gradient(circle at 20px 440px, rgba(29,80,150,0.85) 0 70px, rgba(29,80,150,0) 90px),
      radial-gradient(ellipse at 170px 160px, rgba(29,42,107,0.55) 0%, rgba(60,150,220,0.35) 45%, rgba(60,150,220,0) 75%),
      radial-gradient(circle at 60px 720px, rgba(29,42,107,0.45) 0 40px, rgba(29,42,107,0) 80px),
      linear-gradient(180deg, rgba(90,190,235,0.35), rgba(90,190,235,0) 90%);
    -webkit-mask-image: linear-gradient(90deg, #000 60%, transparent 100%);
    mask-image: linear-gradient(90deg, #000 60%, transparent 100%);
  }

  .forest-art {
    position: absolute; left: 0; top: 755px; width: 900px; height: 228px;
    background:
      linear-gradient(180deg, rgba(217,242,251,0) 0%, #cfe3f2 25%, #8ea6c8 55%, #4c5f92 80%, #dfe8f3 100%);
  }

  .presenter {
    position: absolute; right: 48px; top: 40px; text-align: right;
    font-family: "Crimson Text", serif; font-weight: 600;
    font-size: 25px; line-height: 36px; color: var(--plum);
  }
  .presenter strong { color: var(--ink); font-weight: 600; }
  .presents {
    position: absolute; right: 52px; top: 165px;
    font-family: "Crimson Text", serif; font-weight: 700; font-size: 22px; letter-spacing: 0.5px;
  }
  .title {
    position: absolute; right: 42px; top: 196px;
    font-family: "Yellowtail", "Dancing Script", cursive; font-weight: 400;
    font-size: 100px; color: var(--flame);
    line-height: 1; white-space: nowrap;
  }
  .invite {
    position: absolute; right: 48px; top: 345px; text-align: right;
    font-family: "Montserrat", sans-serif; font-size: 16.5px; line-height: 21px;
  }
  .guests-label {
    position: absolute; right: 48px; top: 428px;
    font-family: "Crimson Text", serif; font-weight: 700; font-size: 22px; color: var(--flame);
  }
  .guests {
    position: absolute; right: 48px; top: 470px; text-align: right;
    font-family: "Crimson Text", serif; font-weight: 700; font-size: 23px; line-height: 27px;
  }
  .dates {
    position: absolute; right: 48px; top: 548px; text-align: right;
    font-family: "Oswald", sans-serif; font-weight: 600; font-size: 52px; line-height: 61px;
    color: var(--plum); letter-spacing: -0.5px; white-space: nowrap;
  }
  .dates .day { color: var(--flame); }
  .venue {
    position: absolute; right: 48px; top: 700px; text-align: right;
    font-family: "Montserrat", sans-serif; font-weight: 500; font-size: 24px; line-height: 32px;
  }

  .tickets-label {
    position: absolute; left: 50px; top: 991px;
    font-family: "Montserrat", sans-serif; font-weight: 500; font-size: 19px; color: var(--violet);
  }
  .ticket-bar {
    position: absolute; left: 42px; top: 1024px; width: 458px; height: 42px;
    background: linear-gradient(180deg, var(--leather-light), var(--leather));
    border-radius: 8px; padding: 3px;
  }
  .ticket-bar .stitch {
    height: 100%; border: 1.5px dashed var(--stitch); border-radius: 6px;
    display: flex; align-items: center; justify-content: space-around;
    font-family: "Roboto", sans-serif; font-size: 18.5px; color: #fff;
  }
  .ticket-bar .divider { width: 1px; height: 22px; background: var(--stitch); }
  .ticket-bar b { font-weight: 500; }

  .brand {
    position: absolute; right: 50px; top: 1030px;
    font-family: "Crimson Text", serif; font-weight: 400; font-size: 36px; color: var(--violet);
    letter-spacing: 1px; white-space: nowrap;
  }

  .credits {
    position: absolute; left: 43px; top: 1075px;
    font-family: "Crimson Text", serif; font-size: 13px; word-spacing: 1px;
  }
  .credits span + span { margin-left: 10px; }
  .childcare {
    position: absolute; left: 43px; top: 1099px;
    font-family: "Montserrat", sans-serif; font-weight: 500; font-size: 14.5px; color: var(--violet);
  }
  .childcare .web { color: var(--ink); font-weight: 400; }
  .nonprofit {
    position: absolute; left: 43px; top: 1125px;
    font-family: "Montserrat", sans-serif; font-size: 13.2px;
  }
</style>
</head>
<body>
  <main class="flyer">
    <div class="ornament-art" role="img" aria-label="Hanging Christmas ornaments: blue swirls, beaded strands, eight-pointed stars and baubles"></div>
    <div class="forest-art" role="img" aria-label="Snow-covered pine forest"></div>

    <p class="presenter"><strong>Lumina Voices:</strong> Choral Artists of<br>the Valley Daniel Hale,<br>Artistic Director</p>
    <p class="presents">PRESENTS</p>
    <h1 class="title">Love and Joy</h1>

    <p class="invite">Join the singers of Lumina Voices as<br>we perform carols,chorales, and other<br>joyful and poignant music of the season!</p>

    <p class="guests-label">WITH SPECIAL GUESTS</p>
    <p class="guests">The Choirs of Ridgeview Middle School<br>Owen Carter, director</p>

    <p class="dates">SATURDAY, <span class="day">DECEMBER 1</span> AT 5:00PM<br>SUNDAY, <span class="day">DECEMBER 2</span> AT 3:00PM</p>

    <p class="venue">Grace Hill Community Church<br>1418 Mesa Verde Avenue NE Riverton</p>

    <p class="tickets-label">Tickets available online &amp; at the door:</p>
    <div class="ticket-bar">
      <div class="stitch">
        <span>General <b>$20</b></span><span class="divider"></span>
        <span>Seniors <b>$15</b></span><span class="divider"></span>
        <span>Students <b>$10</b></span>
      </div>
    </div>

    <p class="brand">LUMINA VOICES</p>

    <p class="credits"><span>Daniel Hale, Artistic Director</span><span>Clara Whitfield, Executive Director</span></p>
    <p class="childcare">Complimentary childcare provided at both performances. <span class="web">www.luminavoices-example.org</span></p>
    <p class="nonprofit">Lumina Voices is a 501(c)3 nonprofit organization, &amp; an Ensemble-in-Residence at Grace Hill Community Church.</p>
  </main>
</body>
</html>
```